Letterhead

We are looking for a basic letterhead. It should include our logo, website - northbaykitchenware.com, phone 907.318.5926, toll free 855.419.2836, and fax 907.318.4150, along with our address 4378 Birchmont Avenue, Anchorage, AK 99612. I want something that will look good printed in color or black and white.

```html
<!DOCTYPE html>
<html lang="en">
<head>
<meta charset="utf-8">
<title>North Bay Kitchenware Letterhead</title>
<link rel="stylesheet" href="https://fonts.googleapis.com/css2?family=Questrial&family=Open+Sans:wght@400;700&display=swap">
<style>
  :root {
    --backdrop: #e9e9e9;
    --paper: #ffffff;
    --ink: #3c3c3c;
    --ink-soft: #6f6f6f;
    --accent: #6e6e6e;
    --accent-light: #9a9a9a;
  }
  * { box-sizing: border-box; margin: 0; padding: 0; }
  html, body {
    width: 1200px; height: 960px; overflow: hidden;
    background: var(--backdrop);
  }
  .letterhead {
    position: absolute; left: 282px; top: 30px;
    width: 636px; height: 900px;
    background: var(--paper);
    box-shadow: 0 4px 18px rgba(0,0,0,0.12);
    font-family: "Questrial", sans-serif;
    color: var(--ink);
  }
  .brand {
    position: absolute; right: 56px; top: 52px;
    display: flex; align-items: center; gap: 10px;
  }
  .brand-mark { width: 14px; height: 14px; background: var(--accent); }
  .brand-name {
    font-size: 22px; letter-spacing: 1px; text-transform: uppercase;
    color: var(--ink);
  }
  .letter-date {
    position: absolute; right: 56px; top: 92px;
    font-size: 10px; color: var(--ink);
  }
  .letter-body {
    position: absolute; left: 64px; top: 200px; width: 500px;
    font-size: 10.5px; line-height: 1.75; color: var(--ink-soft);
  }
  .salutation { color: var(--ink); margin-bottom: 14px; }
  .letter-body p.paragraph { margin-bottom: 22px; }
  .closing { margin-top: 30px; }
  .closing .sign-off { color: var(--ink-soft); }
  .closing .signatory {
    font-family: "Open Sans", sans-serif; font-weight: 700;
    font-size: 9.5px; text-transform: uppercase; color: var(--ink);
  }
  .footer-band {
    position: absolute; left: 0; bottom: 0; width: 230px; height: 96px;
  }
  .contact {
    position: absolute; left: 250px; bottom: 22px;
    font-family: "Open Sans", sans-serif; font-weight: 700;
    font-size: 10px; line-height: 1.45; color: var(--ink);
  }
  .contact .label { display: inline-block; width: 40px; }
</style>
</head>
<body>
  <main class="letterhead">
    <header class="brand">
      <span class="brand-mark"></span>
      <span class="brand-name">North Bay Kitchenware</span>
    </header>
    <p class="letter-date">Date : 08-Nov-14</p>

    <section class="letter-body">
      <p class="salutation">Sir / Madam,</p>
      <p class="paragraph">Lorem ipsum dolor sit amet, consectetur adipiscing elit. Aenean vel placerat nisi, id vestibulum tellus. Proin ligula ipsum, ultrices sit amet justo id, ullamcorper porttitor augue. Nulla sed metus at nunc hendrerit porta. Sed egestas luctus cursus. Etiam commodo turpis nulla, sed ornare augue scelerisque vel. Aliquam erat volutpat. Nam scelerisque tincidunt risus a ultrices. Aenean imperdiet ante mi, vel dictum nibh tempor ac. Nunc auctor ut lorem vel vulputate. Praesent magna nunc, rhoncus ut ipsum eget, ullamcorper auctor nulla. Lorem ipsum dolor sit amet, consectetur adipiscing elit. Aenean vel placerat nisi, id vestibulum tellus. Proin ligula ipsum, ultrices sit amet justo id, ullamcorper porttitor augue. Nulla sed metus at nunc hendrerit porta. Sed egestas luctus cursus. Etiam commodo turpis nulla, sed ornare augue scelerisque vel. Aliquam erat volutpat. Nam scelerisque tincidunt risus a ultrices. Aenean imperdiet ante mi, vel dictum nibh tempor ac. Nunc auctor ut lorem vel vulputate. Praesent magna nunc, rhoncus ut ipsum eget, ullamcorper auctor nulla.</p>
      <p class="paragraph">Phasellus sem justo, suscipit ac laoreet id, tincidunt vel mauris. Nullam vulputate nisi ut sodales pulvinar. Vivamus convallis fringilla arcu non pellentesque. Aenean sed commodo neque. Duis volutpat eleifend sapien, et aliquam quam facilisis eu. Suspendisse viverra nec ligula quis scelerisque. Etiam nibh magna, aliquet vel aliquam quis, fermentum vestibulum nulla. Fusce pellentesque, sem vel tristique pretium, risus elit sodales lectus, non aliquet nunc ipsum et nulla. Nunc sapien neque, pulvinar vel suscipit quis, laoreet non sapien. Phasellus sem justo, suscipit ac laoreet id, tincidunt vel mauris. Nullam vulputate nisi ut sodales pulvinar. Vivamus convallis fringilla arcu non pellentesque. Aenean sed commodo neque. Duis volutpat eleifend sapien, et aliquam quam facilisis eu. Suspendisse viverra nec ligula quis scelerisque. Etiam nibh magna, aliquet vel aliquam quis, fermentum vestibulum nulla. Fusce pellentesque, sem vel tristique pretium, risus elit sodales lectus, non aliquet nunc ipsum et nulla. Nunc sapien neque, pulvinar vel suscipit quis, laoreet non sapien.</p>
      <div class="closing">
        <p class="sign-off">Yours Sicerely</p>
        <p class="signatory">North Bay Kitchenware</p>
      </div>
    </section>

    <svg class="footer-band" viewBox="0 0 230 96" aria-hidden="true">
      <rect x="0" y="40" width="230" height="56" fill="var(--accent)"/>
      <rect x="0" y="30" width="230" height="6" fill="var(--accent-light)"/>
    </svg>

    <address class="contact" style="font-style: normal;">
      4378 Birchmont Avenue,<br>
      Anchorage, AK 99612<br>
      <span class="label">Phone:</span>907.318.5926<br>
      <span class="label">Phone:</span>855.419.2836 (Toll Free)<br>
      <span class="label">Fax:</span>907.318.4150<br>
      www.northbaykitchenware.com
    </address>
  </main>
</body>
</html>
```